Business Card Design

I am in the progress of starting up my business.

Business Name - KT Surface Cleaning

Services that we offer
- Driveway Cleaning
- Foot Path Cleaning
- Pebble & Normal Cement
- Gutter Clean Out
- Removal of Moss & Mould
- Moss & Mould treatment is also available
- Entertainment & Courtyard Area's etc
- Gutter Guard Installation
- Full roof restoration, We Only Use Veltrano Products
- (veltrano application licence, Includes a full 10 year full warrenty )

New Business Card Information - I would like to get rid of "We cover all maitland & Newcastle regions" And Change it to Newcastle Region Hunter Valley Region Nelson Bay Region And the List on the back I would also like to change to OUR SERVICES Driveway & Foot Path Cleaning Treatment & Removal Of Moss & Mould Entertainment & Deck Area's Pebble Crete & cemented Area's Factory & Office Fronts House Exterior (Windows, Veranda's, Brick Work) Roof & Gutter Cleaning Roof Restoration - Veltrano, Korvin Roof Membrane 418 (Veltrano Application Licence, Includes Full 10 Year Warranty)

Industry/Entity Type

Business

Contact Information for Business Card

KT Surface Washing
Water Blasting And Roof Restorations
ABN # 47 219 806 153
Phone # 0417385926
Contact Reid For A Free Quote
Cover Maitland & Newcastle Region's

[Can you please send me an email when you would like me to send through picture as this page wont allow me to add pictures]

Thanks Reid

Requirements
Must have
• Main details on the front of the business card and a picture or two. on the back of the business I would like the list of services that my company provide on the back
Nice to have
• I was hoping that on the front of the business I could have all the company information and details and maybe a picture or two if able to. On the back of the card I would like the services I provide listed but also not over crowded at the same time..

```html
<!DOCTYPE html>
<html lang="en">
<head>
<meta charset="utf-8">
<title>KT Surface Washing – Services Card</title>
<link rel="stylesheet" href="https://fonts.googleapis.com/css2?family=Delius&display=swap">
<style>
  :root {
    --sky-top: #7ea6d8;
    --sky-mid: #a9c5e6;
    --sky-low: #d3e2f1;
    --spray: rgba(255, 255, 255, 0.75);
    --ink: #0b0b0b;
    --accent: #b30000;
    --glow: rgba(255, 255, 255, 0.55);
  }
  html, body {
    margin: 0;
    padding: 0;
    width: 1200px;
    height: 741px;
    overflow: hidden;
  }
  .card {
    position: relative;
    width: 1200px;
    height: 741px;
    overflow: hidden;
    font-family: "Delius", "Comic Sans MS", cursive;
    font-style: italic;
  }
  .card__backdrop {
    position: absolute;
    inset: 0;
    background:
      radial-gradient(ellipse 55% 18% at 62% 30%, var(--spray), transparent 70%),
      radial-gradient(ellipse 45% 30% at 80% 82%, rgba(255,255,255,0.6), transparent 70%),
      linear-gradient(180deg, var(--sky-top) 0%, var(--sky-mid) 45%, var(--sky-low) 100%);
  }
  .services {
    position: absolute;
    left: 54px;
    top: 40px;
    margin: 0;
    padding: 0;
    list-style: none;
    font-size: 38px;
    line-height: 52px;
    color: var(--ink);
    letter-spacing: 1px;
    white-space: nowrap;
    text-shadow: 2px 2px 3px var(--glow);
  }
  .services__title {
    color: var(--accent);
    letter-spacing: 2px;
  }
  .business {
    position: absolute;
    right: 60px;
    top: 44px;
    text-align: right;
    white-space: nowrap;
    text-shadow: 2px 2px 3px var(--glow);
  }
  .business__name {
    display: block;
    font-size: 40px;
    line-height: 48px;
    color: var(--accent);
    letter-spacing: 1px;
  }
  .business__tagline,
  .business__abn {
    display: block;
    font-size: 23px;
    line-height: 32px;
    color: var(--ink);
  }
  .business__quote {
    display: block;
    margin-top: 10px;
    font-size: 28px;
    line-height: 38px;
    color: var(--accent);
  }
  .business__phone {
    display: block;
    font-size: 40px;
    line-height: 48px;
    color: var(--accent);
    letter-spacing: 1px;
  }
  .regions {
    position: absolute;
    right: 60px;
    bottom: 58px;
    margin: 0;
    padding: 0;
    list-style: none;
    text-align: right;
    font-size: 28px;
    line-height: 38px;
    color: var(--accent);
    white-space: nowrap;
    text-shadow: 2px 2px 3px var(--glow);
  }
</style>
</head>
<body>
  <main class="card">
    <div class="card__backdrop" role="img" aria-label="Photo of a pressure-washer water jet arcing across a blue sky with light clouds"></div>

    <ul class="services">
      <li class="services__title">OUR SERVICES</li>
      <li>Driveway &amp; Foot Path Cleaning</li>
      <li>Treatment &amp; Removal Of Moss &amp; Mould</li>
      <li>Entertainment &amp; Deck Area's</li>
      <li>Pebble Crete &amp; cemented Area's</li>
      <li>Factory &amp; Office Fronts</li>
      <li>House Exterior (Windows, Veranda's, Brick Work)</li>
      <li>Roof &amp; Gutter Cleaning</li>
      <li>Roof Restoration - Veltrano,</li>
      <li>Korvin Roof Membrane 418</li>
      <li>(Veltrano Application Licence,</li>
      <li>Includes Full 10 Year Warranty)</li>
    </ul>

    <aside class="business">
      <span class="business__name">KT Surface Washing</span>
      <span class="business__tagline">Water Blasting And Roof Restorations</span>
      <span class="business__abn">ABN # 47 219 806 153</span>
      <span class="business__quote">Contact Reid For A Free Quote</span>
      <span class="business__phone">Phone #0417385926</span>
    </aside>

    <ul class="regions">
      <li>Newcastle Region</li>
      <li>Hunter Valley Region</li>
      <li>Nelson Bay Region</li>
    </ul>
  </main>
</body>
</html>
```